Salt Moon, Tin Heart

Hey Guys
Please visit our Chatterleaf page for the film. See what ideas you bring to the table for the movie poster.
Looking for creative and something fresh.
Check out cast on QVTK
Will use the stills from the film for actual poster and quality.
Thanks a million for taking an interest in our film. xoxo
Target Market(s)
2-50 year old, date night, girls night out
Industry/Entity Type
Movie

```html
<!DOCTYPE html>
<html lang="en">
<head>
<meta charset="utf-8">
<title>Salt Moon, Tin Heart — Poster</title>
<link rel="stylesheet" href="https://fonts.googleapis.com/css2?family=Open+Sans:wght@300;400&display=swap">
<style>
  :root {
    --backdrop: #333333;
    --title-ink: rgba(250, 244, 242, 0.78);
    --credit-ink: rgba(255, 255, 255, 0.92);
    --hair-dark: #3a2e28;
    --skin-warm: #b08468;
    --skin-light: #c9a08a;
    --sea-grey: #9fb0c2;
    --sky-pale: #c3cfdb;
  }
  * { margin: 0; padding: 0; box-sizing: border-box; }
  html, body {
    width: 1200px; height: 1200px; overflow: hidden;
    background: var(--backdrop);
  }
  .poster {
    position: absolute;
    left: 243px; top: 50px;
    width: 714px; height: 1100px;
    overflow: hidden;
    font-family: "Open Sans", Arial, sans-serif;
  }
  .poster-still {
    position: absolute; inset: 0;
    background:
      radial-gradient(ellipse 60% 45% at 25% 18%, var(--hair-dark) 0%, rgba(58,46,40,0) 75%),
      radial-gradient(ellipse 55% 40% at 30% 70%, var(--skin-light) 0%, rgba(201,160,138,0) 80%),
      radial-gradient(ellipse 50% 45% at 95% 85%, var(--sky-pale) 0%, rgba(195,207,219,0) 80%),
      linear-gradient(135deg, #4a3a30 0%, var(--skin-warm) 40%, #a88e80 60%, var(--sea-grey) 100%);
  }
  .title {
    position: absolute;
    left: 0; right: 0; top: 92px;
    text-align: center;
    color: var(--title-ink);
    font-weight: 300;
    font-size: 132px;
    line-height: 192px;
    letter-spacing: 22px;
    text-indent: 22px;
    text-transform: uppercase;
  }
  .title span { display: block; }
  .credits {
    position: absolute;
    left: 0; right: 0; top: 952px;
    text-align: center;
    color: var(--credit-ink);
    font-weight: 400;
    font-size: 16.5px;
    line-height: 22px;
    letter-spacing: 2.2px;
  }
</style>
</head>
<body>
  <main class="poster">
    <div class="poster-still" role="img" aria-label="Film still: a couple in close profile, foreheads touching, by the sea on a bright day"></div>
    <h1 class="title">
      <span>Salt</span>
      <span>Moon</span>
      <span>Tin</span>
      <span>Heart</span>
    </h1>
    <div class="credits">
      <p>Directors: Marla Questov, Tobias Wren Calloway</p>
      <p>Writers: Marla Questov (screenplay), Marla Questov</p>
      <p>Stars: Nadia Fellows, Rhys Amador, Corinne Vale</p>
    </div>
  </main>
</body>
</html>
```